stationary & business cards for medical clinic
Northfield Institute of Rest Care
stationary & business cards for medical clinic - Medical
Creative Brief
Professional
Delia Marsh
Owner
284 Cobblestone Lane Brookhollow, MS 39402
dmarsh@nirestcare.com
www.nirestcare.com
No color or image on envelope flaps please! No full-bleeds on envelopes or letterhead! Full-bleeds are okay on business cards ONLY.

```html
<!DOCTYPE html>
<html lang="en">
<head>
<meta charset="utf-8">
<title>Northfield Institute of Rest Care — Business Card</title>
<link rel="stylesheet" href="https://fonts.googleapis.com/css2?family=Open+Sans:wght@400;600;700&display=swap">
<style>
  :root {
    --backdrop: #e9e6e1;
    --card: #ffffff;
    --brand-blue: #1f8fd1;
    --accent-red: #e63a3d;
    --ink: #2c3f73;
    --muted: #7a7f88;
  }
  * { margin: 0; padding: 0; box-sizing: border-box; }
  html, body {
    width: 1200px; height: 914px; overflow: hidden;
    background: var(--backdrop);
    font-family: "Open Sans", Arial, sans-serif;
  }
  .canvas {
    width: 1200px; height: 914px;
    display: flex; align-items: center; justify-content: center;
  }
  .business-card {
    width: 1000px; height: 572px;
    background: var(--card);
    box-shadow: 0 6px 24px rgba(0,0,0,0.12);
    position: relative;
    display: flex; flex-direction: column; align-items: center;
  }
  .brand {
    margin-top: 92px;
    display: flex; align-items: center; gap: 18px;
  }
  .brand-dot {
    width: 46px; height: 46px; border-radius: 50%;
    background: var(--brand-blue);
  }
  .brand-name {
    font-size: 28px; font-weight: 600; color: var(--brand-blue);
    letter-spacing: 0.5px;
  }
  .person {
    margin-top: 70px;
    display: flex; align-items: baseline; gap: 48px;
    margin-left: -40px;
  }
  .person-name { font-size: 24px; font-weight: 600; color: var(--accent-red); }
  .person-role { font-size: 20px; color: var(--muted); }
  .contacts {
    position: absolute; left: 70px; right: 70px; bottom: 96px;
    display: flex; flex-direction: column; gap: 22px;
  }
  .contact-row { display: flex; gap: 34px; align-items: center; }
  .contact-item {
    display: flex; align-items: center; gap: 9px;
    font-size: 17px; color: var(--ink);
  }
  .contact-icon { width: 22px; height: 22px; flex: none; }
  .contact-icon circle { fill: var(--accent-red); }
  .contact-icon path, .contact-icon rect { fill: #fff; }
</style>
</head>
<body>
<main class="canvas">
  <section class="business-card">
    <div class="brand">
      <span class="brand-dot"></span>
      <span class="brand-name">Northfield Institute of Rest Care</span>
    </div>

    <div class="person">
      <span class="person-name">Delia Marsh</span>
      <span class="person-role">Owner</span>
    </div>

    <div class="contacts">
      <div class="contact-row">
        <div class="contact-item">
          <svg class="contact-icon" viewBox="0 0 22 22"><circle cx="11" cy="11" r="11"/><path d="M7 5.5l2.2-.4 1.2 2.8-1.4 1.1a7 7 0 0 0 3.9 3.9l1.1-1.4 2.8 1.2-.4 2.2c-5 .3-9.7-4.4-9.4-9.4z"/></svg>
          <span>866-555-0142</span>
        </div>
        <div class="contact-item">
          <svg class="contact-icon" viewBox="0 0 22 22"><circle cx="11" cy="11" r="11"/><path d="M11 5l6 5.2h-1.8V16h-3v-3.5h-2.4V16h-3v-5.8H5z"/></svg>
          <span>284 Cobblestone Lane Brookhollow, MS 39402</span>
        </div>
        <div class="contact-item">
          <svg class="contact-icon" viewBox="0 0 22 22"><circle cx="11" cy="11" r="11"/><path d="M5.5 7.5h11v7h-11zM6.5 8.3l4.5 3.4 4.5-3.4v-.3h-9z"/></svg>
          <span>dmarsh@nirestcare.com</span>
        </div>
      </div>
      <div class="contact-row">
        <div class="contact-item">
          <svg class="contact-icon" viewBox="0 0 22 22"><circle cx="11" cy="11" r="11"/><path d="M7 5.5l2.2-.4 1.2 2.8-1.4 1.1a7 7 0 0 0 3.9 3.9l1.1-1.4 2.8 1.2-.4 2.2c-5 .3-9.7-4.4-9.4-9.4z"/></svg>
          <span>601-555-0178</span>
        </div>
        <div class="contact-item">
          <svg class="contact-icon" viewBox="0 0 22 22"><circle cx="11" cy="11" r="11"/><rect x="6" y="9" width="10" height="6" rx="1"/><rect x="8" y="5.5" width="6" height="3"/></svg>
          <span>601-555-0100</span>
        </div>
        <div class="contact-item">
          <svg class="contact-icon" viewBox="0 0 22 22"><circle cx="11" cy="11" r="11"/><path d="M7 5.5l2.2-.4 1.2 2.8-1.4 1.1a7 7 0 0 0 3.9 3.9l1.1-1.4 2.8 1.2-.4 2.2c-5 .3-9.7-4.4-9.4-9.4z"/></svg>
          <span>601-555-0193</span>
        </div>
        <div class="contact-item">
          <svg class="contact-icon" viewBox="0 0 22 22"><circle cx="11" cy="11" r="11"/><path d="M11 5.5a5.5 5.5 0 1 0 0 11 5.5 5.5 0 0 0 0-11zm0 1.3a4.2 4.2 0 1 1 0 8.4 4.2 4.2 0 0 1 0-8.4zM6.8 10.4h8.4v1.2H6.8z"/></svg>
          <span>www.nirestcare.com</span>
        </div>
      </div>
    </div>
  </section>
</main>
</body>
</html>
```